Jewelry Shop Needs a Business Card Design

***We want a very sharp and unforgettable pantone for the Business Card. ***
***We do not want the business card or logo only in black, white and grey color!!!Please provide us a main color as our brand topic! Thanks!! ***

Mabel’s Nook is a Hong Kong based fine jewelry brand.

We want a very nice, simple and elegant business card design for Mabel's Nook Brand. The company's logo has been uploaded already.

You can design with below info:

Dorian Fung
Director
M: +852 94273658
T: +852 35820417
F: +852 35820419
E: dorian.fung@mabelsnook.example
5/F , Harbourlight Tower, 12-18 Orchid Lane, Wan Tung Kok, Kowloon, Hong Kong

Target Market(s)

Mabel’s Nook philosophy is a jewelry icon of young, creative, trendy, fashionable, stylish, energetic, and elegant. For Mabel’s Nook, jewelry is one collection of artworks, the most important items in personal life.

Industry/Entity Type

Jewelry

Requirements
Must have
• We want a very sharp and unforgettable pantone for the Business Card.

```html
<!DOCTYPE html>
<html lang="en">
<head>
<meta charset="UTF-8">
<title>Mabel’s Nook – Business Card</title>
<link href="https://fonts.googleapis.com/css2?family=Questrial&display=swap" rel="stylesheet">
<style>
  :root {
    --page: #ffffff;
    --frame-orange: #ff6a00;
    --frame-yellow: #fff200;
    --red-dark: #620606;
    --red-mid: #b80505;
    --gold: #ffd200;
    --gold-deep: #ffb400;
    --text-gold: #f7c400;
  }
  * { margin: 0; padding: 0; box-sizing: border-box; }
  html, body {
    width: 1200px; height: 900px; overflow: hidden;
    background: var(--page);
    font-family: "Questrial", "Century Gothic", sans-serif;
  }
  .canvas { position: relative; width: 1200px; height: 900px; }

  .card {
    position: absolute; left: 286px; width: 630px; height: 374px;
    background:
      radial-gradient(circle at 100% 0%, var(--frame-yellow) 0, rgba(255,242,0,0) 110px),
      radial-gradient(circle at 0% 100%, var(--frame-yellow) 0, rgba(255,242,0,0) 110px),
      var(--frame-orange);
  }
  .card--front { top: 64px; }
  .card--back { top: 496px; }

  .card__face {
    position: absolute; left: 14px; top: 13px; width: 602px; height: 347px;
    background: linear-gradient(to bottom, var(--red-dark) 0%, var(--red-mid) 48%, var(--red-dark) 100%);
    box-shadow: 3px 3px 2px rgba(40,0,0,0.7);
    color: var(--text-gold);
  }

  .brand-disc {
    position: absolute; border-radius: 50%;
    background: var(--gold);
  }
  .brand-name {
    position: absolute; text-align: center; white-space: nowrap;
    color: var(--gold-deep); text-transform: uppercase;
  }

  .card--front .brand-disc { left: 184px; top: 26px; width: 230px; height: 230px; }
  .card--front .brand-name { left: 0; width: 602px; top: 280px; font-size: 38px; letter-spacing: 4px; }
  .rule { position: absolute; height: 2px; background: var(--gold-deep); }
  .rule--long { left: 110px; width: 382px; top: 328px; }
  .rule--short { left: 182px; width: 238px; top: 335px; }

  .card--back .brand-disc { left: 440px; top: 33px; width: 93px; height: 93px; }
  .card--back .brand-name { left: 386px; width: 202px; top: 134px; font-size: 16px; letter-spacing: 1.5px; }

  .contact {
    position: absolute; left: 29px; top: 65px;
    font-size: 22px; line-height: 29px; letter-spacing: 1px;
    list-style: none;
  }
  .address {
    position: absolute; left: 29px; top: 263px;
    font-size: 22px; line-height: 34px; letter-spacing: 1.3px; font-style: normal;
  }
</style>
</head>
<body>
<main class="canvas">
  <section class="card card--front" aria-label="Card front">
    <div class="card__face">
      <div class="brand-disc" aria-hidden="true"></div>
      <p class="brand-name">Mabel’s Nook</p>
      <div class="rule rule--long"></div>
      <div class="rule rule--short"></div>
    </div>
  </section>

  <section class="card card--back" aria-label="Card back">
    <div class="card__face">
      <ul class="contact">
        <li>Dorian Fung</li>
        <li>Director</li>
        <li>M: +852 94273658</li>
        <li>T: +852 35820417</li>
        <li>F: +852 35820419</li>
        <li>E: dorian.fung@mabelsnook.example</li>
      </ul>
      <address class="address">5/F,Harbourlight Tower, 12-18 Orchid Lane,<br>Wan Tung Kok, Kowloon, Hong Kong</address>
      <div class="brand-disc" aria-hidden="true"></div>
      <p class="brand-name">Mabel’s Nook</p>
    </div>
  </section>
</main>
</body>
</html>
```